I need a sci/tech/business focused podcast cover and logo

We need a podcast cover designed for Vantle FM, a podcast that explore the edges of human understanding and look at the technologies, trends and societal norms shaping our collective future. Here the world’s top minds share their passion projects and how advances in genomics, space travel, connected devices, artificial intelligence and other exponential tech is converging to create the future of tomorrow.

Title: Vantle (or can be Vantle FM depending on what looks better)

Subtitle: Exploring the Edges of Human Understanding

NOTE: Subtitle not necessary. If it looks great we are fine with or without a subtitle

Target Market(s)

business, technologists, scientists, startups
educated

Industry/Entity Type

Tech

Requirements
Should not have
• do not include a microphone!!

```html
<!DOCTYPE html>
<html lang="en">
<head>
<meta charset="utf-8">
<title>Vantle — Podcast Cover</title>
<link href="https://fonts.googleapis.com/css2?family=Inter:wght@700&display=swap" rel="stylesheet">
<style>
  :root {
    --bg: #000000;
    --ink: #ffffff;
    --red: #f44d4f;
    --red-deep: #5a1416;
  }
  html, body {
    margin: 0;
    padding: 0;
    width: 1200px;
    height: 1200px;
    overflow: hidden;
    background: var(--bg);
  }
  .cover {
    display: block;
    width: 1200px;
    height: 1200px;
  }
  .label {
    font-family: "Inter", "Helvetica Neue", Arial, sans-serif;
    font-weight: 700;
    fill: var(--ink);
  }
  .label--kicker { font-size: 66px; letter-spacing: -1px; }
  .label--subtitle { font-size: 66px; letter-spacing: -0.5px; }
  .letter {
    font-family: "Inter", "Helvetica Neue", Arial, sans-serif;
    font-weight: 700;
    font-size: 215px;
    fill: var(--bg);
    text-anchor: middle;
    dominant-baseline: central;
  }
  .title-disc { fill: var(--ink); }
  .field { fill: url(#field-glow); }
</style>
</head>
<body>
<svg class="cover" viewBox="0 0 1500 1500" xmlns="http://www.w3.org/2000/svg" aria-label="Vantle podcast cover">
  <defs>
    <radialGradient id="field-glow" cx="0.48" cy="0.47" r="0.52">
      <stop offset="0" style="stop-color:#f44d4f"/>
      <stop offset="0.35" style="stop-color:#b8383b"/>
      <stop offset="0.75" style="stop-color:#3a0d0e"/>
      <stop offset="1" style="stop-color:#000000"/>
    </radialGradient>
  </defs>

  <rect width="1500" height="1500" fill="var(--bg)"/>

  <rect class="field" x="110" y="120" width="1360" height="1180" role="img"
        aria-label="Decorative field of scattered fading red and white dots with outlined squares"/>

  <g class="title" aria-label="Vantle">
    <circle class="title-disc" cx="232" cy="212" r="126"/>
    <text class="letter" x="232" y="215">V</text>
    <circle class="title-disc" cx="442" cy="438" r="126"/>
    <text class="letter" x="442" y="441">A</text>
    <circle class="title-disc" cx="892" cy="512" r="126"/>
    <text class="letter" x="892" y="515">N</text>
    <circle class="title-disc" cx="1295" cy="210" r="126"/>
    <text class="letter" x="1295" y="213">T</text>
    <circle class="title-disc" cx="1295" cy="750" r="126"/>
    <text class="letter" x="1295" y="753">L</text>
    <circle class="title-disc" cx="785" cy="1118" r="126"/>
    <text class="letter" x="785" y="1121">E</text>
  </g>

  <text class="label label--kicker" x="38" y="90">Podcast</text>
  <text class="label label--subtitle" x="34" y="1378">Exploring the Edges of</text>
  <text class="label label--subtitle" x="34" y="1465">Human Understanding</text>
</svg>
</body>
</html>
```